RP-Steuerberatung WordPress Site fully implemented (tax advisor)

Hello!
I need a little Wordpress Site for my newly founded Tax-Advisor Company.
I am a one-man Office advising in the area of Crypto-Currency.
PLEASE only provide a Design, if you can also Implement a WP-Site afterwards on an existing Webspace.

Please find the Content and Website-Description in the attached Document

Language for the Website is German (for now)

Target Market(s)

Tax-Advisory (specialized in Crypto Currency)

Coding

Coded - Design and coding required

Number of Pages Required

5+ page

Font styles to use
Sans Serif

Requirements
Must have
• Wordpress Implementation afterwards - Details according to attached Project Information Document

```html
<!DOCTYPE html>
<html lang="de">
<head>
<meta charset="utf-8">
<title>RP-Steuerberatung</title>
<link href="https://fonts.googleapis.com/css2?family=Poppins:wght@400;600;800&family=Heebo:wght@400&family=Noto+Serif:wght@500&display=swap" rel="stylesheet">
<style>
  :root {
    --bg-deep: #1d2233;
    --bg-mid: #2b3249;
    --bg-warm: #4a4650;
    --text-light: #ffffff;
    --text-dark: #111111;
    --footer-bg: #171a24;
    --btn-bg: #ffffff;
  }
  * { margin: 0; padding: 0; box-sizing: border-box; }
  html, body { width: 1200px; height: 706px; overflow: hidden; }
  body {
    position: relative;
    background: var(--bg-deep);
    color: var(--text-light);
    font-family: "Heebo", sans-serif;
  }
  .hero-photo {
    position: absolute; inset: 0;
    background:
      radial-gradient(ellipse 340px 260px at 800px 330px, rgba(150,120,110,0.45), transparent 70%),
      radial-gradient(ellipse 500px 400px at 820px 300px, rgba(90,96,130,0.5), transparent 75%),
      linear-gradient(100deg, var(--bg-deep) 0%, var(--bg-mid) 55%, var(--bg-deep) 100%);
  }
  .site-header {
    position: absolute; top: 0; left: 0; width: 100%; height: 100px;
  }
  .brand {
    position: absolute; left: 114px; top: 37px;
    display: flex; align-items: center; gap: 10px;
    font-family: "Poppins", sans-serif; font-weight: 600;
    font-size: 16px; letter-spacing: 0.3px;
  }
  .brand-mark { width: 22px; height: 22px; background: var(--text-light); }
  .main-nav a {
    position: absolute; top: 37px;
    font-family: "Poppins", sans-serif; font-size: 16px;
    color: var(--text-light); text-decoration: none;
  }
  .nav-home { left: 458px; }
  .nav-services { left: 541px; }
  .nav-about { left: 674px; }
  .nav-imprint { left: 789px; }
  .contact-btn {
    position: absolute; left: 951px; top: 21px; width: 138px; height: 52px;
    border-radius: 26px; background: var(--btn-bg); color: var(--text-dark);
    font-family: "Noto Serif", serif; font-weight: 500; font-size: 19px;
    display: flex; align-items: center; justify-content: center;
    text-decoration: none;
  }
  .hero-title {
    position: absolute; left: 111px; top: 114px;
    font-family: "Poppins", sans-serif; font-weight: 800;
    font-size: 51px; line-height: 55px; letter-spacing: 0.5px;
    text-transform: uppercase;
  }
  .hero-lead {
    position: absolute; left: 111px; top: 235px;
    font-size: 15.5px; line-height: 26px;
  }
  .cta-btn {
    position: absolute; left: 111px; top: 312px; width: 300px; height: 60px;
    border-radius: 30px; background: var(--btn-bg); color: var(--text-dark);
    font-family: "Poppins", sans-serif; font-weight: 600; font-size: 14px;
    display: flex; align-items: center; justify-content: center;
    text-decoration: none; letter-spacing: 0.2px;
  }
  .myth-list {
    position: absolute; left: 113px; top: 397px; list-style: none;
    font-size: 14px; line-height: 26px;
  }
  .myth-list li { display: flex; align-items: center; gap: 9px; }
  .myth-list li::before {
    content: ""; width: 12px; height: 12px; border-radius: 50%;
    background: var(--text-light); flex: none;
  }
  .site-footer {
    position: absolute; left: 0; top: 639px; width: 100%; height: 67px;
    background: var(--footer-bg);
    display: flex; align-items: center; justify-content: center;
    font-size: 14.5px;
  }
</style>
</head>
<body>
  <div class="hero-photo" role="img" aria-label="Foto: Hände halten ein Tablet, darüber ein leuchtendes, steigendes Balkendiagramm"></div>

  <header class="site-header">
    <div class="brand"><span class="brand-mark"></span>RP STEUERBERATUNG</div>
    <nav class="main-nav">
      <a class="nav-home" href="#">Home</a>
      <a class="nav-services" href="#">Leistungen▾</a>
      <a class="nav-about" href="#">Über mich</a>
      <a class="nav-imprint" href="#">Impressum</a>
    </nav>
    <a class="contact-btn" href="#">Kontakt</a>
  </header>

  <main>
    <h1 class="hero-title">Willkommen bei<br>RP-Steuerberatu</h1>
    <p class="hero-lead">Ihrem Spezialisten bei allen steuerlichen Themen<br>rund um Einkünfte &amp; Vermögen aus Krypto-Assets.</p>
    <a class="cta-btn" href="#">WEITER ZU UNSEREN LEISTUNGEN</a>
    <ul class="myth-list">
      <li>Dann mach ich eine Schweizer Holding-Gesellschaft– dort zahlt man fast keine Steuern</li>
      <li>Dann melde ich einfach meinen Hauptwohnsitz in Österreich ab</li>
      <li>Dann lass ich meine Kryptos auf einer Börse in Singapur, dort ist das steuerfrei</li>
    </ul>
  </main>

  <footer class="site-footer">copyright@2022.RP STEUERBERATU.Alle Rechte vorbehalten</footer>
</body>
</html>
```